FixyFellas,com Home Maintenance Membership Website

Fixy Fellas is a yearly home maintenance membership website where Home Owners, Contractor, and Subcontractors can interact in an online bidding environment to exchange goods and services.

Our Tag Line Is: We Tackle The Weekend Lists That Other Fellas Won't Tackle
Updates

Target Market(s)

Homeowner, Female, 26 to 56 years of age. Middle to upper income.
Contractors/Subcontractors

Industry/Entity Type

Environment

Font styles to use
Other font styles liked:
• We want to match the logo font

Requirements
Must have
• Three-tiered membership plans for homeowners. Features and pricing TBD
Three major customer components as well as a administration back end. The three main components will be Home Owners Page, Contractors/Subcontractors pages, and the request-for Work Pages.
Need Membership levels panel similar to the uploaded picture
We did like this site as a start point. http://www.coatguardprime.example/
Nice to have
• #1: Customer domain profiles for contractors
#2: Blog
#3: Affiliate Program
#4: Contractor Rating System
#5: Internal Messaging System
#6: Banner Ads
#7: Escrow Payments

```html
<!DOCTYPE html>
<html lang="en">
<head>
<meta charset="utf-8">
<title>Fixy Fellas – Home Maintenance Membership</title>
<link rel="stylesheet" href="https://fonts.googleapis.com/css2?family=Lato:wght@300;400;700;900&family=Ultra&display=swap">
<style>
:root{
  --orange:#f25a0a;
  --navy:#2e3947;
  --ink:#2b2f36;
  --text:#555b63;
  --muted:#9aa1aa;
  --panel:#eeeeee;
  --section:#efefef;
  --line:#e2e2e2;
  --footer:#3a3a3a;
  --wood:#d49a5c;
  --white:#ffffff;
}
*{box-sizing:border-box;margin:0;padding:0}
html,body{width:1200px;height:2587px;overflow:hidden}
body{position:relative;background:var(--white);font-family:"Lato",Arial,sans-serif;color:var(--text)}
.abs{position:absolute}
/* header */
.hero-photo{left:0;top:0;width:1200px;height:600px;background:linear-gradient(180deg,#f4f4f4 0%,#e9e4df 22%,#c9a58a 55%,#b07a5a 80%,#d9c9bd 100%)}
.header-fade{left:0;top:0;width:1200px;height:135px;background:linear-gradient(180deg,#fff 0%,rgba(255,255,255,.85) 60%,rgba(255,255,255,0) 100%)}
.brand{display:flex;align-items:center;gap:8px;font-family:"Lato",sans-serif;font-weight:900;color:var(--navy);font-size:20px}
.brand-dot{width:34px;height:34px;border-radius:50%;background:var(--orange)}
.nav{left:604px;top:32px;display:flex;gap:0;font-size:13px;color:#3c4450}
.nav a{color:inherit;text-decoration:none;padding:5px 8px;margin-right:22px;border:1px solid transparent}
.nav a.active{border-color:var(--orange);border-radius:2px}
.search{left:1084px;top:36px}
/* hero */
.hero-band{left:268px;top:233px;width:692px;height:208px;background:rgba(60,66,78,.78);text-align:center;color:#fff}
.hero-kicker{margin-top:36px;font-size:17px;letter-spacing:4px;font-weight:400}
.hero-title{font-weight:300;font-size:80px;letter-spacing:12px;line-height:1;margin-top:8px;position:relative}
.hero-title .accent{color:var(--orange)}
.hero-rule{position:absolute;top:40px;height:2px;width:60px;background:var(--orange)}
.hero-sub{font-size:19px;letter-spacing:4px;margin-top:8px}
.wood{left:0;top:600px;width:1200px;height:86px;background:linear-gradient(180deg,#e2b178,#c98c4f 60%,#d7a16a)}
.tagline{left:0;top:600px;width:1200px;line-height:86px;text-align:center;font-weight:900;font-size:27px;letter-spacing:2.5px;color:#2a2622}
/* feature boxes */
.feature{top:721px;width:289px;height:204px;background:var(--panel);text-align:center}
.diamond{position:absolute;left:50%;top:-14px;width:40px;height:40px;margin-left:-20px;background:var(--navy);transform:rotate(45deg);border:3px solid #fff}
.diamond svg{transform:rotate(-45deg);margin-top:9px}
.feature h3{margin-top:48px;font-size:15px;color:var(--ink);font-weight:700}
.feature p{margin-top:10px;font-size:11.5px;line-height:21px;color:var(--text)}
.btn{display:inline-block;background:var(--orange);color:#fff;font-size:11px;padding:8px 16px;margin-top:14px}
/* services / contact */
.section-title{font-weight:900;font-size:26px;color:var(--ink);letter-spacing:.5px}
.copy{font-size:11.5px;line-height:21px;color:var(--text)}
.acc-active{left:124px;top:1058px;width:464px;height:31px;background:var(--navy);color:#fff;font-size:12px;line-height:31px;padding-left:8px}
.acc-row{left:124px;width:464px;height:34px;border:1px solid var(--line);font-size:11px;font-weight:700;color:#3c4450;line-height:32px;padding-left:6px}
.acc-row svg{position:absolute;right:8px;top:9px}
.contact-line{left:612px;font-size:11.5px;color:var(--text);display:flex;align-items:center;gap:10px}
.field{border:1px solid #dcdcdc;background:#fff;font-size:11.5px;color:#666;padding-left:18px;line-height:31px}
.field svg{position:absolute;right:10px;top:10px}
.submit{left:612px;top:1250px;width:462px;height:32px;background:var(--orange);color:#fff;font-weight:900;font-size:12px;text-align:center;line-height:32px}
/* pricing */
.pricing-bg{left:0;top:1300px;width:1200px;height:555px;background:var(--section)}
.block-title{font-weight:900;font-size:25px;letter-spacing:2px;color:var(--ink);text-align:center}
.block-sub{font-size:11.5px;line-height:21px;color:#b3b8be;text-align:center}
.plan{top:1435px;width:230px;height:398px;background:#fff;text-align:center}
.plan-head{height:48px;background:var(--orange);color:#fff;font-weight:900;font-size:21px;letter-spacing:2px;line-height:48px}
.plan-price{height:47px;background:#e9eced;color:#2b2f36;font-size:26px;line-height:47px}
.plan-price sup{font-size:12px}
.plan-price small{font-size:11px}
.plan-row{height:34.5px;line-height:34.5px;border-bottom:1px solid #eee;font-size:11.5px;color:#a8aeb4}
.buy{position:absolute;left:29px;bottom:12px;width:172px;height:38px;background:var(--orange);color:#fff;font-weight:900;font-size:13px;line-height:38px}
.plan.featured{top:1428px;left:610px;width:237px;height:415px;border:4px solid var(--navy)}
.plan.featured .plan-head{background:#e6e9ec;color:var(--navy)}
.plan.featured .plan-price{background:var(--orange);color:#fff}
.plan.featured .buy{background:var(--navy);left:30px}
.ribbon{position:absolute;right:-4px;top:-4px;width:46px;height:46px;overflow:hidden}
.ribbon span{position:absolute;right:-18px;top:9px;width:76px;transform:rotate(45deg);background:#9aa3ad;color:#fff;font-size:9px;font-weight:900;text-align:center;line-height:14px}
.rating{left:863px;top:1432px;width:231px;height:314px;background:#fff}
.rating-head{height:46px;background:var(--navy);color:#fff;font-size:12px;line-height:46px;padding-left:16px;position:relative}
.rating-head svg{position:absolute;right:16px;top:15px}
.photo-contractor{left:17px;top:51px;width:197px;height:121px;background:linear-gradient(160deg,#e7c24a,#c9a675 45%,#9fb5c7)}
.rating h4{position:absolute;left:17px;top:200px;font-size:14px;color:var(--ink);font-weight:700}
.stars{position:absolute;left:17px;top:232px;display:flex;gap:2px}
.view{position:absolute;left:64px;top:276px;width:89px;height:24px;background:#a9afb6;color:#fff;font-size:11px;line-height:24px;text-align:center}
.badge{left:863px;top:1760px;width:231px;height:69px;background:#c6cacd;display:flex;align-items:center;justify-content:center}
.badge-shape{width:150px;height:34px;border-radius:17px;background:#9ca3a8}
/* blog */
.post{top:1993px;width:464px;height:165px;background:#f6f6f6}
.post-rail{position:absolute;left:0;top:0;width:35px;height:165px;background:var(--navy)}
.rail-cell{height:33px;border-bottom:1px solid #3e4a59;display:flex;align-items:center;justify-content:center}
.rail-cell.first{background:var(--orange)}
.rail-date{color:#fff;text-align:center;font-size:14px;font-weight:700;line-height:14px;padding-top:6px}
.rail-date small{display:block;font-size:9px;font-weight:400}
.post-img{position:absolute;left:35px;top:0;width:197px;height:165px}
.post-body{position:absolute;left:248px;top:12px;width:205px}
.post-body h5{font-size:14px;color:var(--ink);font-weight:700}
.post-body .role{font-size:11px;color:#b3b8be;margin-top:6px}
.post-body p{font-size:11.5px;line-height:19px;color:#b3b8be;margin-top:10px}
.ad{left:135px;top:2201px;width:927px;height:145px;background:#c8c8c8;text-align:center;line-height:145px;font-family:"Ultra",serif;font-size:38px;color:#1f4e8a}
.ad .hot{color:var(--orange)}
/* footer */
.footer{left:0;top:2369px;width:1200px;height:218px;background:var(--footer);border-bottom:4px solid var(--orange)}
.foot-title{font-size:16px;font-weight:700;color:#fff}
.foot-title::after{content:"";display:block;width:130px;height:1px;background:#666;margin-top:6px;box-shadow:0 1px 0 #444}
.foot-title span{display:block;width:18px;height:2px;background:var(--orange);margin-top:4px}
.foot-item{font-size:11px;color:#fff;line-height:15px;display:flex;gap:8px;align-items:flex-start}
.foot-list li{list-style:none;font-size:11px;color:#fff;line-height:27px;display:flex;align-items:center;gap:8px}
.foot-list li.on{color:var(--orange)}
.social{left:148px;top:2519px;display:flex;gap:14px}
.social span{width:12px;height:12px;border-radius:50%;background:#dcdcdc;display:block}
.sub-input{border:1px solid var(--orange);height:28px;width:182px;font-size:10px;color:#999;line-height:26px;padding-left:8px}
.sub-btn{background:var(--orange);color:#fff;font-size:11px;width:72px;height:26px;line-height:26px;text-align:center}
</style>
</head>
<body>

<!-- hero -->
<div class="abs hero-photo" role="img" aria-label="Photo of many raised hands holding tools: drills, tape measures, wrenches, levels and set squares"></div>
<div class="abs header-fade"></div>
<div class="abs brand" style="left:152px;top:48px"><span class="brand-dot"></span>FixyFellas.com</div>
<nav class="abs nav">
  <a class="active">Home</a><a>About</a><a>Services</a><a>Blog</a><a>Features</a><a>Contact</a>
</nav>
<svg class="abs search" width="16" height="16" viewBox="0 0 16 16"><circle cx="9" cy="7" r="5" fill="none" stroke="#9aa1aa" stroke-width="1.5"/><line x1="5.5" y1="10.5" x2="1.5" y2="14.5" stroke="#9aa1aa" stroke-width="1.5"/></svg>

<div class="abs hero-band">
  <div class="hero-kicker">WOULD YOU LIKE TO BE</div>
  <div class="hero-title"><span class="hero-rule" style="left:32px"></span>CRE<span class="accent">A</span>TIVE<span class="hero-rule" style="right:32px"></span></div>
  <div class="hero-sub">WITH AMAZING WORK</div>
</div>

<div class="abs wood" role="img" aria-label="Wooden plank texture"></div>
<div class="abs tagline">We Tackle The Weekend Lists That Other Fellas Won't Tackle</div>

<!-- features -->
<div class="abs feature" style="left:131px">
  <div class="diamond"><svg width="16" height="16" viewBox="0 0 16 16"><path d="M3 9a5 5 0 0 1 10 0" fill="none" stroke="#fff" stroke-width="1.6"/><rect x="2" y="9" width="3" height="5" fill="#fff"/><rect x="11" y="9" width="3" height="5" fill="#fff"/></svg></div>
  <h3>Fast Online Support</h3>
  <p>Praesent turpis mauris, aliquet id dolor<br>Gravida adipiscing lectus ut rutrum<br>Aenean at posuere risus.</p>
  <span class="btn">Read more</span>
</div>
<div class="abs feature" style="left:458px">
  <div class="diamond"><svg width="16" height="16" viewBox="0 0 16 16"><circle cx="8" cy="8" r="4.5" fill="none" stroke="#fff" stroke-width="3" stroke-dasharray="2.4 1.2"/><circle cx="8" cy="8" r="1.6" fill="#fff"/></svg></div>
  <h3>Services</h3>
  <p>Praesent turpis mauris, aliquet id dolor<br>Gravida adipiscing lectus ut rutrum<br>Aenean at posuere risus.</p>
  <span class="btn">Read more</span>
</div>
<div class="abs feature" style="left:783px">
  <div class="diamond"><svg width="16" height="16" viewBox="0 0 16 16"><path d="M14 2L6 6 2 8l4 2 2 4 2-4z" fill="#fff"/></svg></div>
  <h3>Affiliate Program</h3>
  <p>Praesent turpis mauris, aliquet id dolor<br>Gravida adipiscing lectus ut rutrum<br>Aenean at posuere risus.</p>
  <span class="btn">Read more</span>
</div>

<!-- services -->
<h2 class="abs section-title" style="left:128px;top:952px">OUR SERVICES</h2>
<p class="abs copy" style="left:132px;top:995px;width:460px">Suspendisse sed eros mollis, tincidunt felis eget, interdum erat. Nullam sit amet odio eu est aliquet euismod a a urna. Proin eu urna suscipit, dictum quam nec.</p>
<div class="abs acc-active">Renovating</div>
<p class="abs copy" style="left:128px;top:1100px;width:460px">Lorem ipsum dolor sit amet, consectetur adipiscing elit. Proin eu est ut augue pulvinar mattis vitae quis magna. In mollis sem nec ullamcorper luctus. Ut tellus tellus, imperdiet vel augue sit amet.</p>
<div class="abs acc-row" style="top:1176px">Painting &amp; Decorating<svg width="16" height="16" viewBox="0 0 16 16"><circle cx="8" cy="8" r="7" fill="none" stroke="#bbb"/><path d="M8 4v8M4 8h8" stroke="#bbb"/></svg></div>
<div class="abs acc-row" style="top:1210px">Carpentary<svg width="16" height="16" viewBox="0 0 16 16"><circle cx="8" cy="8" r="7" fill="none" stroke="#bbb"/><path d="M8 4v8M4 8h8" stroke="#bbb"/></svg></div>
<div class="abs acc-row" style="top:1244px">Repairs &amp; Maintenance<svg width="16" height="16" viewBox="0 0 16 16"><circle cx="8" cy="8" r="7" fill="none" stroke="#bbb"/><path d="M8 4v8M4 8h8" stroke="#bbb"/></svg></div>

<!-- keep in touch -->
<h2 class="abs section-title" style="left:612px;top:956px">KEEP IN TOUCH</h2>
<p class="abs copy" style="left:612px;top:995px;width:462px">Suspendisse sed eros mollis, tincidunt felis eget, interdum erat. Nullam sit amet odio eu est aliquet euismod a a urna.</p>
<div class="abs contact-line" style="top:1055px"><svg width="13" height="10" viewBox="0 0 13 10"><rect width="13" height="10" fill="#9aa1aa"/><path d="M0 0l6.5 5L13 0" fill="none" stroke="#fff"/></svg>hello@fixyfellas.example</div>
<div class="abs contact-line" style="top:1081px"><svg width="13" height="12" viewBox="0 0 13 12"><path d="M6.5 0L0 6h2v6h3.5V8h2v4H11V6h2z" fill="#9aa1aa"/></svg>27 Lantern Row, Suite 4, Maplewood</div>
<div class="abs contact-line" style="top:1107px"><svg width="13" height="13" viewBox="0 0 13 13"><path d="M3 0l2 3-1.5 1.5a8 8 0 0 0 5 5L10 8l3 2-1.5 3C6 13 0 7 0 1.5z" fill="#9aa1aa"/></svg>+1 555 014 2270</div>
<div class="abs field" style="left:612px;top:1146px;width:237px;height:33px">Name<svg width="8" height="13" viewBox="0 0 8 13"><rect x="1.5" width="5" height="8" rx="2.5" fill="#bbb"/><path d="M0 6a4 4 0 0 0 8 0M4 10v3" fill="none" stroke="#bbb"/></svg></div>
<div class="abs field" style="left:861px;top:1146px;width:213px;height:33px">Email<svg width="13" height="10" viewBox="0 0 13 10"><rect width="13" height="10" fill="#bbb"/><path d="M0 0l6.5 5L13 0" fill="none" stroke="#fff"/></svg></div>
<div class="abs field" style="left:612px;top:1190px;width:462px;height:52px"></div>
<div class="abs submit">SUBMIT NOW</div>

<!-- pricing -->
<div class="abs pricing-bg"></div>
<h2 class="abs block-title" style="left:280px;top:1313px;width:400px">PRICING TABLE</h2>
<p class="abs block-sub" style="left:280px;top:1354px;width:400px">Our design is coupled with the excellent value<br>Aliquam sit amet hendrerit non, placerat pulvinar enim</p>
<h2 class="abs block-title" style="left:863px;top:1313px;width:210px">RATING</h2>
<p class="abs block-sub" style="left:855px;top:1354px;width:226px">Our design is coupled with the excellen- value Aliquam sit amet hendrerit non, placerat pulvinar enim</p>

<div class="abs plan" style="left:116px">
  <div class="plan-head">BASIC</div>
  <div class="plan-price"><sup>$</sup>99<small>/month</small></div>
  <div class="plan-row">1 Hosting</div><div class="plan-row">2 Email Marketing</div><div class="plan-row">5 databases</div><div class="plan-row">2 Design Pack</div><div class="plan-row">3 Website Layouts</div><div class="plan-row">5 Header Style</div><div class="plan-row" style="border:0">3 Online Store</div>
  <div class="buy">BUY NOW</div>
</div>
<div class="abs plan" style="left:363px">
  <div class="plan-head">ULTIMATE</div>
  <div class="plan-price"><sup>$</sup>199<small>/month</small></div>
  <div class="plan-row">1 Hosting</div><div class="plan-row">2 Email Marketing</div><div class="plan-row">5 databases</div><div class="plan-row">2 Design Pack</div><div class="plan-row">3 Website Layouts</div><div class="plan-row">5 Header Style</div><div class="plan-row" style="border:0">3 Online Store</div>
  <div class="buy">BUY NOW</div>
</div>
<div class="abs plan featured">
  <div class="ribbon"><span>HOT</span></div>
  <div class="plan-head">STANDARD</div>
  <div class="plan-price"><sup>$</sup>299<small>/month</small></div>
  <div class="plan-row">1 Hosting</div><div class="plan-row">2 Email Marketing</div><div class="plan-row">5 databases</div><div class="plan-row">2 Design Pack</div><div class="plan-row">3 Website Layouts</div><div class="plan-row">5 Header Style</div><div class="plan-row" style="border:0">3 Online Store</div>
  <div class="buy">BUY NOW</div>
</div>

<div class="abs rating">
  <div class="rating-head">Contractor Rating<svg width="18" height="15" viewBox="0 0 18 15"><path d="M4 1h10l3 4-8 9-8-9z M1 5h16 M6 1l3 13 3-13" fill="none" stroke="#fff" stroke-width="1.3"/></svg></div>
  <div class="abs photo-contractor" role="img" aria-label="Photo of a smiling contractor in a hard hat with his crew"></div>
  <h4>Contractor Rating</h4>
  <div class="stars">
    <svg width="14" height="14" viewBox="0 0 24 24"><path d="M12 1l3.4 7 7.6 1-5.5 5.3 1.3 7.6L12 18.3 5.2 21.9l1.3-7.6L1 9l7.6-1z" fill="var(--orange)"/></svg>
    <svg width="14" height="14" viewBox="0 0 24 24"><path d="M12 1l3.4 7 7.6 1-5.5 5.3 1.3 7.6L12 18.3 5.2 21.9l1.3-7.6L1 9l7.6-1z" fill="var(--orange)"/></svg>
    <svg width="14" height="14" viewBox="0 0 24 24"><path d="M12 1l3.4 7 7.6 1-5.5 5.3 1.3 7.6L12 18.3 5.2 21.9l1.3-7.6L1 9l7.6-1z" fill="var(--orange)"/></svg>
    <svg width="14" height="14" viewBox="0 0 24 24"><path d="M12 1l3.4 7 7.6 1-5.5 5.3 1.3 7.6L12 18.3 5.2 21.9l1.3-7.6L1 9l7.6-1z" fill="var(--orange)"/></svg>
    <svg width="14" height="14" viewBox="0 0 24 24"><path d="M12 1l3.4 7 7.6 1-5.5 5.3 1.3 7.6L12 18.3 5.2 21.9l1.3-7.6L1 9l7.6-1z" fill="none" stroke="var(--orange)" stroke-width="2"/><path d="M12 1v17.3L5.2 21.9l1.3-7.6L1 9l7.6-1z" fill="var(--orange)"/></svg>
  </div>
  <div class="view">View detail</div>
</div>
<div class="abs badge"><div class="badge-shape"></div></div>

<!-- blog -->
<h2 class="abs block-title" style="left:300px;top:1880px;width:600px">RECENT POST FROM BLOG</h2>
<p class="abs block-sub" style="left:300px;top:1920px;width:600px">Our design is coupled with the excellent value<br>Aliquam sit amet hendrerit non, placerat pulvinar enim</p>

<div class="abs post" style="left:126px">
  <div class="post-rail">
    <div class="rail-cell first"><svg width="14" height="11" viewBox="0 0 14 11"><rect x=".5" y=".5" width="13" height="10" fill="none" stroke="#fff"/><path d="M2 9l3-4 3 3 2-2 2 3z" fill="#fff"/></svg></div>
    <div class="rail-cell"><svg width="10" height="12" viewBox="0 0 10 12"><circle cx="5" cy="3" r="3" fill="#fff"/><path d="M0 12a5 5 0 0 1 10 0z" fill="#fff"/></svg></div>
    <div class="rail-cell"><svg width="12" height="11" viewBox="0 0 12 11"><path d="M6 11L1 6a3 3 0 0 1 5-4 3 3 0 0 1 5 4z" fill="#fff"/></svg></div>
    <div class="rail-date">24<small>Jan</small></div>
  </div>
  <div class="post-img" role="img" aria-label="Photo of hands raising assorted hand tools over a wooden plank" style="background:linear-gradient(135deg,#f3efe9,#d3a679 55%,#b7784a)"></div>
  <div class="post-body"><h5>Your Blog Title Here</h5><div class="role">Contractor</div><p>Donec mattis felis sit amet viverra elementum. Nullam rutrum sit amet nisl eu rhoncus. Duis tristique dolor magna, vitae mattis mauris</p></div>
</div>
<div class="abs post" style="left:614px">
  <div class="post-rail">
    <div class="rail-cell first"><svg width="14" height="11" viewBox="0 0 14 11"><rect x=".5" y=".5" width="13" height="10" fill="none" stroke="#fff"/><path d="M2 9l3-4 3 3 2-2 2 3z" fill="#fff"/></svg></div>
    <div class="rail-cell"><svg width="10" height="12" viewBox="0 0 10 12"><circle cx="5" cy="3" r="3" fill="#fff"/><path d="M0 12a5 5 0 0 1 10 0z" fill="#fff"/></svg></div>
    <div class="rail-cell"><svg width="12" height="11" viewBox="0 0 12 11"><path d="M6 11L1 6a3 3 0 0 1 5-4 3 3 0 0 1 5 4z" fill="#fff"/></svg></div>
    <div class="rail-date">24<small>Jan</small></div>
  </div>
  <div class="post-img" role="img" aria-label="Photo of a worker wearing a tool belt holding pliers" style="background:linear-gradient(135deg,#f2f2f2,#9a6b4a 50%,#c9802f)"></div>
  <div class="post-body"><h5>Your Blog Title Here</h5><div class="role">Contractor</div><p>Donec mattis felis sit amet viverra elementum. Nullam rutrum sit amet nisl eu rhoncus. Duis tristique dolor magna, vitae mattis mauris</p></div>
</div>

<div class="abs ad">Advertise <span class="hot">Your Business</span> Here!</div>

<!-- footer -->
<footer class="abs footer"></footer>
<div class="abs brand" style="left:128px;top:2424px;color:#fff"><span class="brand-dot"></span>FixyFellas.com</div>
<div class="abs social"><span></span><span></span><span></span><span></span><span></span></div>

<div class="abs" style="left:384px;top:2400px">
  <div class="foot-title">Contact</div>
  <div class="foot-item" style="margin-top:16px"><svg width="8" height="11" viewBox="0 0 8 11"><path d="M4 11L.6 5.5A4 4 0 1 1 7.4 5.5z" fill="#fff"/></svg><span>18 Birchfield Avenue, Floor 3<br>Cedar Falls,<br>ST 00412</span></div>
  <div class="foot-item" style="margin-top:14px"><svg width="10" height="10" viewBox="0 0 13 13"><path d="M3 0l2 3-1.5 1.5a8 8 0 0 0 5 5L10 8l3 2-1.5 3C6 13 0 7 0 1.5z" fill="#fff"/></svg>555 019 4482</div>
  <div class="foot-item" style="margin-top:14px"><svg width="11" height="8" viewBox="0 0 13 10"><rect x=".5" y=".5" width="12" height="9" fill="none" stroke="#fff"/><path d="M0 0l6.5 5L13 0" fill="none" stroke="#fff"/></svg>info@fixyfellas.example</div>
</div>

<div class="abs" style="left:624px;top:2400px">
  <div class="foot-title">Resources</div>
  <ul class="foot-list" style="margin-top:6px">
    <li class="on">&raquo; Repairs &amp; Maintenance</li>
    <li>&raquo; Carpentary</li>
    <li>&raquo; Fencing</li>
    <li>&raquo; Out Doors</li>
  </ul>
</div>

<div class="abs" style="left:868px;top:2400px;width:200px">
  <div class="foot-title">Subscribe</div>
  <p style="font-size:10.5px;line-height:14px;color:#fff;margin-top:12px">Subscribe to our newsletter to receive news, updates, free stuff and new releases by email. We don't do spam.</p>
  <div class="sub-input" style="margin-top:10px">Enter your email address</div>
  <div style="display:flex;justify-content:space-between;align-items:center;margin-top:12px;width:182px">
    <svg width="30" height="20" viewBox="0 0 30 20"><rect x="1" y="1" width="28" height="18" fill="#ddd"/><path d="M1 1l14 10L29 1" fill="none" stroke="#999"/></svg>
    <div class="sub-btn">Subscribe</div>
  </div>
</div>

</body>
</html>
```